Website update for Harbor Broker Ledger & Payroll Services

Our website needs updating
www.harborbrokerledgers.com
Here are some of our latest print pieces to use as a guide?
I have also attached our graphic identity guide which includes the Pantone colors

Target Market(s)

Insurance Agencies

Industry/Entity Type

Accounting

Number of Pages Required

5+ page

```html
<!DOCTYPE html>
<html lang="en">
<head>
<meta charset="utf-8">
<title>Harbor Broker Ledger &amp; Payroll Services</title>
<link href="https://fonts.googleapis.com/css2?family=Open+Sans:wght@300;400;600;700&display=swap" rel="stylesheet">
<style>
:root{
  --teal:#1bb3a2;
  --teal-dark:#12937f;
  --ink:#333;
  --muted:#666;
  --band:#ececec;
  --footer:#2a2a2a;
  --white:#fff;
}
*{box-sizing:border-box;margin:0;padding:0}
html,body{width:1200px;height:2316px;overflow:hidden}
body{position:relative;font-family:"Open Sans",sans-serif;color:var(--ink);background:var(--white)}
.abs{position:absolute}
.site-header{left:0;top:0;width:1200px;height:92px;background:var(--white)}
.brand{left:36px;top:16px;display:flex;align-items:center;gap:12px}
.brand-mark{width:56px;height:56px;background:var(--teal)}
.brand-name{font-size:20px;font-weight:700;color:var(--teal);line-height:1.15;width:300px}
.social-top{right:50px;top:12px;display:flex;gap:12px}
.social-top span{width:22px;height:22px;border-radius:50%;background:var(--teal)}
.main-nav{left:416px;top:48px;display:flex;font-size:15px}
.main-nav a{color:var(--ink);text-decoration:none;padding:10px 15px}
.main-nav a.active{background:var(--teal);color:var(--white)}
.hero{left:0;top:92px;width:1200px;height:612px;background:linear-gradient(135deg,#dfe4e6,#f6f6f6 45%,#b9c0c4)}
.hero-arrow{top:370px;font-size:40px;color:var(--white);font-weight:700}
.hero-dots{left:560px;top:640px;display:flex;gap:10px}
.hero-dots span{width:16px;height:16px;border-radius:50%;background:rgba(255,255,255,.7)}
.hero-dots span.on{background:var(--white);box-shadow:0 0 0 2px var(--teal)}
.about{left:0;top:704px;width:1200px;height:336px;background:var(--white)}
.about-panel{left:380px;top:12px;width:780px;height:312px;background:var(--band)}
.portrait{left:80px;top:14px;width:320px;height:306px;background:linear-gradient(180deg,#7a5a45,#c7a48a 55%,#6ea56a)}
.about h2{left:440px;top:34px;font-size:40px;font-weight:600;color:var(--ink)}
h2 em,.services h2 em{font-style:normal;color:var(--teal)}
.about p{left:440px;top:96px;width:680px;font-size:15px;line-height:1.6;color:var(--muted)}
.btn{display:inline-block;background:var(--teal);color:var(--white);font-size:14px;padding:9px 22px;border-radius:3px;border-bottom:3px solid var(--teal-dark)}
.about .btn{left:440px;top:226px}
.services{left:0;top:1040px;width:1200px;height:580px;background:var(--band)}
.services h2{left:0;top:40px;width:1200px;text-align:center;font-size:44px;font-weight:600}
.card{top:140px;width:312px;height:410px;background:var(--white);text-align:center}
.card h3{height:50px;line-height:50px;background:var(--teal);color:var(--white);font-size:17px;font-weight:600}
.card .photo{margin:14px auto 0;width:284px;height:180px}
.card p{margin:16px 20px 0;font-size:14px;line-height:1.5;color:var(--muted);height:64px}
.card .btn{margin-top:22px}
.tagline{left:0;top:1620px;width:1200px;height:300px;text-align:center}
.tagline h2{margin-top:64px;font-size:30px;font-weight:300;line-height:1.35;color:var(--ink)}
.tagline p{margin-top:18px;font-size:15px;color:var(--muted);line-height:1.5}
.tagline .btn{margin-top:22px}
.site-footer{left:0;top:1920px;width:1200px;height:360px;background:var(--footer);color:#ddd}
.site-footer h4{font-size:28px;font-weight:300;color:var(--white)}
.contact{left:80px;top:40px;width:330px}
.contact ul{list-style:none;margin-top:20px;font-size:13px;line-height:1.5}
.contact li{display:flex;gap:12px;margin-bottom:14px}
.contact svg{flex:none;margin-top:2px}
.map{left:432px;top:64px;width:330px;height:236px;background:linear-gradient(135deg,#e8e4da,#d3dccb)}
.news{left:830px;top:40px;width:300px}
.news p{font-size:13px;margin-top:20px}
.news .field{margin-top:10px;display:flex;height:34px}
.news .field span{flex:1;background:var(--white);color:#999;font-size:13px;line-height:34px;padding-left:10px}
.news .field b{width:40px;background:var(--teal)}
.news .follow{margin-top:24px;font-size:14px}
.social-foot{margin-top:10px;display:flex;gap:12px}
.social-foot span{width:28px;height:28px;border-radius:50%;background:var(--teal)}
.copyright{left:0;top:2280px;width:1200px;height:36px;background:var(--teal);color:var(--white);font-size:13px;text-align:center;line-height:36px}
</style>
</head>
<body>
<header class="site-header abs">
  <div class="brand abs"><span class="brand-mark"></span><span class="brand-name">Harbor Broker Ledger &amp; Payroll Services</span></div>
  <div class="social-top abs"><span></span><span></span><span></span></div>
  <nav class="main-nav abs">
    <a class="active">Home</a><a>About Us</a><a>Compare</a><a>Our Services</a><a>How It Works</a><a>Resources</a><a>Blog</a><a>Contact Us</a>
  </nav>
</header>

<section class="hero abs" role="img" aria-label="Business professionals shaking hands across an office desk">
  <span class="hero-arrow abs" style="left:24px">&laquo;</span>
  <span class="hero-arrow abs" style="left:1152px">&raquo;</span>
  <div class="hero-dots abs"><span></span><span class="on"></span><span></span></div>
</section>

<section class="about abs">
  <div class="about-panel abs"></div>
  <div class="portrait abs" role="img" aria-label="Portrait of the firm's founding accountant"></div>
  <h2 class="abs"><em>Know</em> About Us</h2>
  <p class="abs">Marla Quinlan is an Accounting Professional with more than 20 years experience in accounting, budgeting and financial reporting for independent insurance agencies. She has a proven track record of improving efficiency in agency bookkeeping and implementing technology initiatives throughout her career.</p>
  <span class="btn abs">Read More</span>
</section>

<section class="services abs">
  <h2 class="abs"><em>Our</em> Services</h2>
  <article class="card abs" style="left:88px">
    <h3>Book keeping tasks</h3>
    <div class="photo" role="img" aria-label="Calculator and pen resting on financial papers" style="background:linear-gradient(135deg,#cfd8dc,#f2f4f5)"></div>
    <p>Direct bill commission deposits reconciled and recorded</p>
    <span class="btn">Read More</span>
  </article>
  <article class="card abs" style="left:444px">
    <h3>Financial statements prepared</h3>
    <div class="photo" role="img" aria-label="Printed financial charts and a calculator" style="background:linear-gradient(135deg,#9fc3e0,#eef3f7)"></div>
    <p>Balance Sheet, Income Statement (compared with prior and budget)</p>
    <span class="btn">Read More</span>
  </article>
  <article class="card abs" style="left:800px">
    <h3>Sample of special projects</h3>
    <div class="photo" role="img" aria-label="Office team gathered around a laptop" style="background:linear-gradient(135deg,#d8d4cf,#6b6f75)"></div>
    <p>Clean up of general ledger accounts, Temporary assistance during staff</p>
    <span class="btn">Read More</span>
  </article>
</section>

<section class="tagline abs">
  <h2>Experienced team of insurance agency bookkeeping professionals<br>maintaining your books</h2>
  <p>Affordable, professional services for less than the cost of an in-house<br>bookkeeper and Capabilities</p>
  <span class="btn">Learn More</span>
</section>

<footer class="site-footer abs">
  <div class="contact abs">
    <h4>Keep In Touch</h4>
    <ul>
      <li><svg width="14" height="18" viewBox="0 0 14 18"><path d="M7 0a7 7 0 0 0-7 7c0 5 7 11 7 11s7-6 7-11a7 7 0 0 0-7-7zm0 10a3 3 0 1 1 0-6 3 3 0 0 1 0 6z" fill="#fff"/></svg><span>Harbor Broker Ledger &amp; Payroll Services<br>48 Wharfside Lane<br>Eastport, CT 06790</span></li>
      <li><svg width="14" height="14" viewBox="0 0 14 14"><path d="M3 0l3 3-2 2c1 2 3 4 5 5l2-2 3 3-2 3C6 14 0 8 0 3z" fill="#fff"/></svg><span>860-555-0142</span></li>
      <li><svg width="14" height="14" viewBox="0 0 14 14"><rect x="1" y="4" width="12" height="8" fill="#fff"/><rect x="3" y="0" width="8" height="5" fill="#fff"/></svg><span>877-555-0199</span></li>
      <li><svg width="14" height="12" viewBox="0 0 14 12"><rect width="14" height="12" fill="#fff"/><path d="M0 0l7 6 7-6" stroke="#2a2a2a" fill="none"/></svg><span>info@harborbrokerledgers.com</span></li>
    </ul>
  </div>
  <div class="map abs" role="img" aria-label="Street map showing the office location"></div>
  <div class="news abs">
    <h4>NewsLatter</h4>
    <p>Signing Here for our Email updates</p>
    <div class="field"><span>Email</span><b></b></div>
    <p class="follow">Follow Us</p>
    <div class="social-foot"><span></span><span></span><span></span></div>
  </div>
</footer>
<div class="copyright abs">&copy; Harbor Broker Ledger - 2015. All rights reserved.</div>
</body>
</html>
```